Amber Hollow Productions

I need a business card design for a new freelance film production company using or incorporating the logo:
I want the card to be creative, minimal, yet professional. Feel free to use a variety of different shapes and sizes/ textures for the card.

Industry/Entity Type

Film Production

```html
<!DOCTYPE html>
<html lang="en">
<head>
<meta charset="utf-8">
<title>Amber Hollow Productions – Business Card</title>
<link rel="stylesheet" href="https://fonts.googleapis.com/css2?family=Questrial&display=swap">
<style>
  :root {
    --card-bg: #ffffff;
    --brand-blue: #0c56a6;
    --ink-black: #000000;
    --text-grey: #555555;
  }
  html, body {
    margin: 0;
    padding: 0;
    overflow: hidden;
    background: var(--card-bg);
  }
  .card {
    position: relative;
    width: 1200px;
    height: 720px;
    background: var(--card-bg);
    overflow: hidden;
    font-family: "Questrial", "Century Gothic", sans-serif;
    color: var(--text-grey);
  }
  .top-band {
    position: absolute;
    left: 0;
    width: 100%;
  }
  .top-band--blue {
    top: 78px;
    height: 16px;
    background: var(--brand-blue);
  }
  .top-band--black {
    top: 101px;
    height: 8px;
    background: var(--ink-black);
  }
  .sweep {
    position: absolute;
    left: 0;
    top: 0;
  }
  .sweep__shadow { fill: var(--ink-black); }
  .sweep__fill { fill: var(--brand-blue); }
  .contact-line,
  .company-name,
  .address-line {
    position: absolute;
    margin: 0;
    white-space: nowrap;
    line-height: 1;
    font-weight: 400;
  }
  .contact-line { font-size: 36px; }
  .contact-line--email { left: 105px; top: 162px; }
  .contact-line--phone { left: 108px; top: 205px; }
  .company-name {
    left: 109px;
    top: 344px;
    font-size: 44px;
  }
  .address-line { font-size: 35px; left: 111px; }
  .address-line--street { top: 403px; }
  .address-line--region { top: 446px; }
</style>
</head>
<body>
  <main class="card">
    <div class="top-band top-band--blue"></div>
    <div class="top-band top-band--black"></div>

    <svg class="sweep" width="1200" height="720" viewBox="0 0 1200 720" aria-hidden="true">
      <path class="sweep__shadow" d="M0,717 C500,655 950,505 1200,237 L1200,720 L0,720 Z"/>
      <path class="sweep__fill" d="M30,720 C520,664 980,527 1200,286 L1200,720 Z"/>
    </svg>

    <p class="contact-line contact-line--email">email:hello@amberhollow.com</p>
    <p class="contact-line contact-line--phone">call: 234-555-0186</p>

    <h1 class="company-name">Amber Hollow Productions</h1>
    <p class="address-line address-line--street">Address: 48#,Cedar Park,</p>
    <p class="address-line address-line--region">USA, 546-210-774</p>
  </main>
</body>
</html>
```